Bluewater Getaways KT needs a new Website

We have an old website that is just that - old. We need a fresh website that is professional graphic designed that has the following features.
1. Can be updated by ourselves in some areas.
2. Has a shopping cart.
3. Has links to download PDF files
4. Has links to other pages in the website
5. Includes social media links
6. Has a client log-in area
Full details in brief provided.

SORRY BUT IT'S URGENT. We've taken too long to write the details and it is now urgent. So my apologies I will be asking for designers to work quickly.

We will continue to use our existing web hosting company and url. Their is a link to the old website in the Design Brief.
Updates

UPDATE:  Please see the new file UPDATE TO DESIGN BRIEF.
Thanks for all your submissions to date.  We hope the update will assist with your designs.
As indicated in previous messages, we are happy with the Home Page + 1 Page in order to select the designer to work with in creating the full design. 

Thankyou Designers.  Much appreciate your efforts.
It's getting late here on Norfolk so I won't have much chance too review any more designs this evening.
But for your information:
Designer 7318405 Ravindra Mehta is so far the closest to what we are seeking.
Thanks again. 

Reason: Have extended to Monday 7 October to give time for designers to submit after feedback today. Especially given the time differences

Target Market(s)

Very wide audience. Current client group not that tech savvy, but we hope to broaden our market and sell more creative products, and so website needs to consider how people now use media, ie tablets & iphones.

Industry/Entity Type

Shopping

Requirements
Nice to have
• PLEASE SEE THE "UPDATE TO THE DESIGN BRIEF"

```html
<!DOCTYPE html>
<html lang="en">
<head>
<meta charset="utf-8">
<title>Bluewater Getaways KT</title>
<link href="https://fonts.googleapis.com/css2?family=Overpass:wght@400;600;700;800&family=Source+Sans+3:wght@300;400&display=swap" rel="stylesheet">
<style>
:root{
  --orange:#f47f20;
  --green:#11a046;
  --teal:#8ee3d2;
  --purple:#9b12a8;
  --yellow:#f2ee00;
  --blue:#1a13d8;
  --text:#555;
  --panel:rgba(70,78,90,.72);
  --panel-field:rgba(90,98,110,.9);
  --white:#fff;
}
*{margin:0;padding:0;box-sizing:border-box}
html,body{width:927px;height:1200px;overflow:hidden;background:var(--white)}
body{position:relative;font-family:"Source Sans 3",sans-serif;color:var(--text)}
a{color:inherit}

.site-header{position:absolute;left:0;top:0;width:927px;height:96px}
.brand{position:absolute;left:26px;top:24px;display:flex;align-items:center;gap:10px}
.brand-mark{width:22px;height:22px;border-radius:50%;background:var(--orange)}
.brand-name{font-family:"Overpass",sans-serif;font-weight:800;font-size:19px;line-height:1.05;color:var(--orange);width:150px}
.cart{position:absolute;left:698px;top:20px;display:flex;align-items:center;gap:8px;font-family:"Overpass",sans-serif;font-weight:700;font-size:10px;color:var(--orange);text-decoration:underline}
.social{position:absolute;top:18px;width:30px;height:30px;border:2px solid var(--green);border-radius:50%;display:flex;align-items:center;justify-content:center;font-family:"Overpass",sans-serif;font-size:8px;font-weight:700;color:var(--green)}
.main-nav{position:absolute;top:71px;left:0;width:927px;font-family:"Overpass",sans-serif;font-weight:700;font-size:9.5px;color:var(--green)}
.main-nav a{position:absolute;text-decoration:none;white-space:nowrap}
.main-nav .active{color:var(--orange)}
.main-nav .active::after{content:"";position:absolute;left:-5px;right:-5px;top:15px;height:3px;background:var(--green)}

.hero{position:absolute;left:0;top:96px;width:927px;height:424px;
  background:linear-gradient(180deg,#2f7fd6 0%,#7fb8ea 22%,#cfe6f6 33%,#3fb7c9 40%,#2fd0cc 55%,#5ee0d4 78%,#8fe8dc 100%)}
.search{position:absolute;left:24px;top:12px;display:flex;align-items:center;gap:6px;color:var(--white);font-size:9px}
.search-icon{width:20px;height:20px;border:1.5px solid var(--white);border-radius:50%;display:flex;align-items:center;justify-content:center}
.dropdown{position:absolute;left:335px;top:4px;width:84px;height:97px;background:var(--panel);font-family:"Overpass",sans-serif;font-size:6px;color:var(--green);text-align:center}
.dropdown a{display:block;text-decoration:none;height:27px;line-height:29px;border-bottom:1px solid rgba(255,255,255,.15)}
.login{position:absolute;left:720px;top:35px;width:168px;height:177px;background:var(--panel);font-family:"Overpass",sans-serif;font-size:5.5px;color:#ddd}
.field{position:absolute;left:19px;width:131px;height:18px;background:var(--panel-field);padding:6px 13px;letter-spacing:.3px}
.login-action{position:absolute;top:130px;display:flex;align-items:center;gap:8px;font-weight:700}
.login-action i{width:13px;height:13px;border:1px solid #bbb;border-radius:50%;display:block}
.signup{color:#3ee0e0}
.remember{position:absolute;left:20px;top:152px;display:flex;align-items:center;gap:8px}
.remember i{width:4px;height:4px;background:#bbb;display:block}
.forgot{position:absolute;left:95px;top:152px;color:#999}
.dots{position:absolute;left:850px;top:402px;display:flex;gap:2px}
.dots i{width:12px;height:12px;border:2px solid var(--white);border-radius:50%;background:rgba(255,255,255,.25);display:block}

.intro{position:absolute;left:0;top:548px;width:927px;text-align:center}
.intro h1{font-family:"Overpass",sans-serif;font-weight:600;font-size:27px;color:#555;letter-spacing:.5px;line-height:32px}
.established{font-size:14px;font-weight:300;color:#555;line-height:12px}
.promotes{margin-top:24px;font-size:17px;font-weight:300;text-decoration:underline;text-underline-offset:3px}
.values{margin-top:12px;font-size:14px;font-weight:300}
.supported{margin-top:36px;font-size:14px;font-weight:300}

.services{position:absolute;top:748px;left:0;width:927px}
.service{position:absolute;width:130px;text-align:center}
.service .tile{width:85px;height:85px;border:4px solid currentColor;margin:0 auto;display:flex;align-items:center;justify-content:center}
.service .label{font-size:19px;font-weight:400;margin-top:16px}

.audience{position:absolute;left:0;width:927px;text-align:center;font-size:13px;font-weight:300;line-height:17px}

.site-footer{position:absolute;left:0;top:1058px;width:927px;height:142px;background:var(--orange);color:var(--white);border-top:1px solid #f9a55e}
.site-footer h2{font-family:"Overpass",sans-serif;font-weight:700;font-size:11px;text-decoration:underline;position:absolute;white-space:nowrap}
.site-footer p{position:absolute;font-size:8px;line-height:10px;font-weight:400;white-space:nowrap}
.right{text-align:right}
</style>
</head>
<body>

<header class="site-header">
  <div class="brand"><span class="brand-mark"></span><span class="brand-name">Bluewater Getaways KT</span></div>
  <a class="cart" href="#">
    <svg width="28" height="26" viewBox="0 0 28 26" aria-hidden="true"><path d="M1 3h5l4 14h13l3-10H8" fill="none" stroke="#f47f20" stroke-width="2.5"/><circle cx="11" cy="22" r="2.5" fill="#f47f20"/><circle cx="21" cy="22" r="2.5" fill="#f47f20"/></svg>
    SHOP CART
  </a>
  <a class="social" style="left:812px" href="#">Like</a>
  <a class="social" style="left:858px" href="#">Post</a>
  <nav class="main-nav">
    <a style="left:286px" href="#">HOME</a>
    <a class="active" style="left:351px" href="#">OVERVIEW</a>
    <a style="left:430px" href="#">KESTREL ISLAND</a>
    <a style="left:549px" href="#">SERVICE</a>
    <a style="left:626px" href="#">OUR SHOP</a>
    <a style="left:705px" href="#">MAKE A BOOKING</a>
    <a style="left:822px" href="#">TESTIMONIAL</a>
  </nav>
</header>

<section class="hero" role="img" aria-label="Photograph of a turquoise lagoon beach with pine trees under a blue sky">
  <div class="search"><span class="search-icon"><svg width="10" height="10" viewBox="0 0 10 10"><circle cx="4" cy="4" r="3" fill="none" stroke="#fff" stroke-width="1.3"/><path d="M6 6l3 3" stroke="#fff" stroke-width="1.3"/></svg></span>search</div>
  <div class="dropdown">
    <a href="#">GOVERNANCE</a>
    <a href="#">OUR MISSION &amp; VALUES</a>
    <a href="#">OUR FACILITATORS</a>
  </div>
  <form class="login">
    <div class="field" style="top:23px">USERNAME</div>
    <div class="field" style="top:47px">EMAIL</div>
    <div class="field" style="top:71px">PASSWORD</div>
    <div class="field" style="top:95px">CONFIRM PASSWORD</div>
    <div class="login-action" style="left:20px"><i></i>LOGIN</div>
    <div class="login-action signup" style="left:79px"><i></i>SIGN UP</div>
    <div class="remember"><i></i>REMEMBER ME</div>
    <div class="forgot">FORGOT PASSWORD</div>
  </form>
  <div class="dots"><i></i><i></i><i></i><i></i></div>
</section>

<section class="intro">
  <h1>OUR SOCIAL ENTERPRISE</h1>
  <p class="established">established July 2001</p>
  <p class="promotes">promotes</p>
  <p class="values">Diversity * Caring * Community * Kestrel Island</p>
  <p class="supported">Supported</p>
</section>

<section class="services">
  <div class="service" style="left:94px;color:var(--orange)">
    <div class="tile"><svg width="56" height="56" viewBox="0 0 56 56"><path d="M50 8c-3-3-8 0-11 3l-8 8-22-6-4 4 18 10-9 9-7-1-3 3 9 5 5 9 3-3-1-7 9-9 10 18 4-4-6-22 8-8c3-3 6-8 3-11z" fill="currentColor"/></svg></div>
    <div class="label">holidays</div>
  </div>
  <div class="service" style="left:238px;color:var(--teal)">
    <div class="tile"><svg width="46" height="46" viewBox="0 0 46 46"><circle cx="23" cy="23" r="19" fill="none" stroke="currentColor" stroke-width="3"/><path d="M23 9l3 14-3 14-3-14z" fill="currentColor"/></svg></div>
    <div class="label">travel</div>
  </div>
  <div class="service" style="left:383px;color:var(--purple)">
    <div class="tile"><svg width="56" height="56" viewBox="0 0 56 56"><path d="M20 8c12-4 26 4 30 18L20 8z" fill="currentColor"/><path d="M20 8c14 0 28 8 30 18-8-6-14-4-15 2-4-6-10-7-15-2 2-6-2-12 0-18z" fill="currentColor"/><path d="M33 20L10 48" stroke="currentColor" stroke-width="3"/></svg></div>
    <div class="label">recreation</div>
  </div>
  <div class="service" style="left:527px;color:var(--yellow)">
    <div class="tile"><svg width="48" height="48" viewBox="0 0 48 48" fill="none" stroke="currentColor" stroke-width="3"><circle cx="24" cy="24" r="20"/><ellipse cx="24" cy="24" rx="9" ry="20"/><path d="M4 24h40M7 14h34M7 34h34M24 4v40"/></svg></div>
    <div class="label">respite</div>
  </div>
  <div class="service" style="left:672px;color:var(--blue)">
    <div class="tile"><svg width="56" height="56" viewBox="0 0 56 56" fill="currentColor"><path d="M22 8h12l7 12 5-3-4 13-13-3 5-3-5-9-6 10-9-5z"/><path d="M8 34l6-10 9 5-6 10h12v-6l10 9-10 9v-6H14c-4 0-8-5-6-11z"/><path d="M48 34l-5-9 9-5 3 6c2 5-1 10-6 12l-2 1z"/></svg></div>
    <div class="label">creative projects</div>
  </div>
</section>

<p class="audience" style="top:923px">for people requiring support to participate in socially inclusive events.</p>
<p class="audience" style="top:972px">Intellectual Disability / Acquired Brain Injury / Mental Health / Sensory Impairment / Frail Aged /<br>Mobility Challenged / Siblings of children with Disabilities</p>

<footer class="site-footer">
  <h2 style="left:21px;top:19px">Location &amp;Contacts</h2>
  <p style="left:21px;top:47px">Harbour Lane, Reef Point<br>PO Box 518<br>Kestrel Island KT 4172<br>SOUTH PACIFIC<br>N.B.N. 481 207 655</p>
  <h2 style="left:149px;top:19px">Telephone</h2>
  <p style="left:149px;top:43px">International +67 23 51807<br>Australia 1800 614 382</p>
  <h2 style="left:149px;top:77px">Email &nbsp;Website &nbsp;&amp; &nbsp;Social</h2>
  <p style="left:149px;top:101px">hello@bluewatergetaways.org www.bluewatergetaways.org<br>social.example/bluewatergetaways</p>
  <p class="right" style="right:13px;top:21px;font-weight:700;font-family:'Overpass',sans-serif">Images &amp; Video</p>
  <p class="right" style="right:13px;top:43px"><u>BLUEWATER VIDEO</u><br>to see more photographs and videos</p>
  <h2 style="right:13px;top:75px">Open Frame Film Festival</h2>
  <p class="right" style="right:13px;top:128px;font-size:5px">copyright bluewater 2013</p>
</footer>

</body>
</html>
```